Wedding invitation

We need a wedding invitation designed with a logo using our initials and name underneath.
We are getting married at THE BRENNA hotel in Gstaad and we would like have our logo similar to theirs but incorporating our initials n&g (any font/case) and our names below noreen and Gilberto. THE BRENNA logo can be seen on their website.
The invitation would be square with the logo on the front in stamped foil and the colour would be THE BRENNA brown (I have the exact colour)
THE BRENNA Brown: C45 M70 Y68 K77
THE BRENNA Rose Gold: VELMAR 218
Inside we would have the invitation wording and on the opposite side some contact info. There would be four inserts - accom, directions, brunch and RSVP. We will provide the wording.

```html
<!DOCTYPE html>
<html lang="en">
<head>
<meta charset="utf-8">
<title>Noreen and Gilberto – Wedding Invitation</title>
<link rel="stylesheet" href="https://fonts.googleapis.com/css2?family=Handlee&display=swap">
<style>
  :root {
    --ink-brown: #9a6a44;
    --seal-white: #ffffff;
    --names-white: #fffaf2;
    --sky-blue: #a9c2e6;
    --sky-lilac: #d9cbe4;
    --sky-peach: #f6c9b4;
    --horizon-rose: #f7c3a8;
    --sea-gold: #f3dcae;
    --sand-light: #f6e6bd;
    --sand-warm: #e9cf9e;
  }
  * { margin: 0; padding: 0; box-sizing: border-box; }
  html, body {
    width: 1200px;
    height: 1200px;
    overflow: hidden;
  }
  .invitation-card {
    position: relative;
    width: 1200px;
    height: 1200px;
    overflow: hidden;
    font-family: "Handlee", cursive;
  }
  .beach-scene {
    position: absolute;
    inset: 0;
    background:
      linear-gradient(180deg,
        var(--sky-blue) 0%,
        var(--sky-lilac) 18%,
        var(--sky-peach) 42%,
        var(--horizon-rose) 60%,
        var(--sea-gold) 62%,
        var(--sand-light) 78%,
        var(--sand-warm) 100%);
  }
  .invitation-title {
    position: absolute;
    top: 130px;
    left: 0;
    width: 100%;
    text-align: center;
    font-size: 86px;
    font-weight: 400;
    letter-spacing: 0.14em;
    color: var(--ink-brown);
  }
  .monogram-seal {
    position: absolute;
    left: 427px;
    top: 500px;
    width: 346px;
    height: 346px;
    border-radius: 50%;
    background: var(--seal-white);
  }
  .monogram-initials {
    position: absolute;
    top: 98px;
    left: 0;
    width: 100%;
    text-align: center;
    font-size: 70px;
    letter-spacing: 0.06em;
    color: var(--ink-brown);
  }
  .monogram-rule {
    position: absolute;
    left: 30px;
    top: 222px;
  }
  .couple-names {
    position: absolute;
    right: 52px;
    bottom: 80px;
    font-size: 40px;
    letter-spacing: 0.13em;
    color: var(--names-white);
  }
</style>
</head>
<body>
  <main class="invitation-card">
    <div class="beach-scene" role="img" aria-label="Photograph of a sunset beach with a bride and groom walking hand in hand at the water's edge"></div>

    <h1 class="invitation-title">Invitation</h1>

    <div class="monogram-seal">
      <p class="monogram-initials">N &amp; G</p>
      <svg class="monogram-rule" width="286" height="44" viewBox="0 0 286 44">
        <line x1="0" y1="4" x2="286" y2="4" stroke="#9a6a44" stroke-width="1.5"/>
        <rect x="20" y="12" width="246" height="26" rx="13" fill="#9a6a44" fill-opacity="0.18" role="img" aria-label="Decorative scroll flourish"/>
      </svg>
    </div>

    <p class="couple-names">Noreen and Gilberto</p>
  </main>
</body>
</html>
```